Web development comapny Business cards/Stationery
Business cards and stationery
Web development comapny Business cards/Stationery  -
Creative Brief
Use specific fonts
Whatever you think looks best
Professional
Dov Marom
חותיפו קוויש להנמ
רחוב הלבן 42, א.ת. רמת נוגה / Halavan 42 St, Ramat Noga
USA only (888)-555-0147
Israel (076)-555-0183 / USA (315)-555-0162
Dov Marom (052)-555-0139
dov@bright-loom.co.il
www.bright-loom.co.il
We building website for SEO in google and facebook so we like the two icons on the front side of the business card. Our main business target is Google SEO service! The business card and envelope should be in red and black. This is a sample work that i like: http://www.pixelharbor.example/drafts/display/contest/81000/draft/618709. I like also to have a silver line in the head and footer of the business card. Please use this Hebrew line in the center of the business card: .קובסייפו לגוגב םירתא םודיקו חוריא היינב חותיפ ןונכת
Please use this text in the back of the business card along with the comany logo: .הרזח ךפסכ תא לבק ונקפיס אל .תחתופה היישימחב םוקימל תוירחא ללוכ לגוגב ינגרוא םודיק תורש תקפסמש לארשיב הדיחיה הרבחה ,טנרטניאה תשרב םירתא םודיקו חוריא חותיפ ןונכת
vantor9 vantor9
Hi PH, Please check your inbox.
kmbelfort kmbelfort
Please don't copy my design@quillpepper
brightloom brightloom
I like this back of the card #24 with this front #20. Can anybody make this work for me? Also please add the envelope and letter head. Thanks, Yoni Tamir
Thank you for your hard work. I really like all your work and it will be very hard to choose only one design. Please add to your designs an envelope and letter like in draft #29. Thanks, Yoni Tamir
Please make sure to include this info in the business card front: .קובסייפו לגוגב םירתא םודיקו חוריא היינב חותיפ ןונכת Please make sure to include this info in the business card back: .הרזח ךפסכ תא לבק ונקפיס אל .תחתופה היישימחב םוקימל תוירחא ללוכ לגוגב ינגרוא םודיק תורש תקפסמש לארשיב הדיחיה הרבחה ,טנרטניאה תשרב םירתא םודיקו חוריא חותיפ ןונכת Please don't use the logo slogan again in the bussiness card.
All the designers are welcome to work on both of our projects Logo design in this URL http://orders.markforge.example/contests/logo-design-for-brightloom

```html
<!DOCTYPE html>
<html lang="en">
<head>
<meta charset="utf-8">
<title>brightloom stationery</title>
<link href="https://fonts.googleapis.com/css2?family=Heebo:wght@400;700&display=swap" rel="stylesheet">
<style>
:root{
  --bg:#3a3a3a;
  --ink:#111111;
  --ink-soft:#2a2a2a;
  --red:#c8141b;
  --red-dark:#7a0a0e;
  --paper:#ffffff;
  --silver:#b9b9b9;
  --grey:#777777;
  --faint:#f3e6e2;
}
*{box-sizing:border-box;margin:0;padding:0}
html,body{width:1200px;height:770px;overflow:hidden;background:var(--bg);font-family:"Heebo",Arial,sans-serif}
.canvas{position:relative;width:1200px;height:770px}
.piece{position:absolute;overflow:hidden;box-shadow:0 4px 12px rgba(0,0,0,.45)}
.brand{display:flex;align-items:center;gap:6px;font-weight:700;letter-spacing:.5px;white-space:nowrap}
.brand-square{display:inline-block;background:var(--red)}
.he{direction:rtl;white-space:nowrap}

/* business card front */
.card-front{width:245px;height:137px;background:linear-gradient(160deg,var(--ink-soft),var(--ink) 60%);color:var(--paper)}
.card-front .silver{position:absolute;left:0;right:0;height:2px;background:var(--silver)}
.card-front .silver.top{top:6px}
.card-front .wave{position:absolute;left:0;bottom:0;width:245px;height:137px}
.card-front .brand{position:absolute;left:12px;top:16px;font-size:14px}
.card-front .brand-square{width:12px;height:12px}
.card-front .tagline{position:absolute;left:12px;top:36px;font-size:5.5px;color:var(--silver)}
.card-front .person{position:absolute;right:12px;top:60px;text-align:right;font-size:9px;font-weight:700}
.card-front .person small{display:block;font-size:5.5px;font-weight:400;color:var(--silver)}
.card-front .contacts{position:absolute;left:12px;top:58px;font-size:5px;line-height:8px;color:var(--paper)}

/* business card back */
.card-back{width:125px;height:137px;background:radial-gradient(circle at 60% 45%,var(--red),var(--red-dark))}
.card-back .strip{position:absolute;left:0;top:0;bottom:0;width:16px;background:var(--ink)}
.card-back .mark{position:absolute;left:46px;top:42px;width:52px;height:52px;background:rgba(0,0,0,.18)}

/* letterhead */
.letterhead{left:660px;top:48px;width:456px;height:672px;background:var(--paper)}
.letterhead .brand{position:absolute;left:24px;top:24px;font-size:20px;color:var(--ink)}
.letterhead .brand-square{width:18px;height:18px}
.letterhead .tagline{position:absolute;left:24px;top:52px;font-size:6px;color:var(--grey)}
.letterhead .head-info{position:absolute;right:20px;top:28px;font-size:5.5px;line-height:9px;color:var(--grey);text-align:right}
.letterhead .mark{position:absolute;left:168px;top:230px;width:120px;height:120px;background:var(--faint)}
.letterhead .foot{position:absolute;left:0;bottom:0;width:456px;height:160px}

/* envelope */
.envelope{left:48px;top:480px;width:576px;height:233px;background:linear-gradient(180deg,var(--ink-soft),var(--ink))}
.envelope .flap{position:absolute;left:0;top:0;width:60px;height:233px;background:linear-gradient(90deg,var(--red),var(--red-dark))}
.envelope .flap-dot{position:absolute;left:28px;top:108px;width:14px;height:14px;background:var(--ink);border-radius:50%}
.envelope .brand{position:absolute;left:90px;top:40px;font-size:24px;color:var(--paper)}
.envelope .brand-square{width:20px;height:20px}
.envelope .tagline{position:absolute;left:90px;top:72px;font-size:6px;color:var(--silver)}
.envelope .mark{position:absolute;left:356px;top:44px;width:110px;height:110px;background:rgba(255,255,255,.05)}
.envelope .silver{position:absolute;left:60px;right:0;bottom:36px;height:1px;background:var(--silver)}
.envelope .foot-info{position:absolute;left:90px;bottom:14px;display:flex;gap:26px;font-size:5.5px;color:var(--silver);white-space:nowrap}
</style>
</head>
<body>
<main class="canvas">

  <!-- business cards, row 1 -->
  <section class="piece card-front" style="left:91px;top:103px">
    <svg class="wave" viewBox="0 0 245 137" aria-hidden="true"><path d="M0 110 Q120 96 245 70 L245 137 L0 137 Z" fill="var(--red)"/></svg>
    <div class="silver top"></div>
    <div class="brand"><span class="brand-square"></span>brightloom</div>
    <p class="tagline he">תכנון פיתוח בניית אירוח וקידום אתרים במנועי חיפוש וברשתות.</p>
    <div class="contacts">
      <p>USA only (888)-555-0147</p>
      <p>Israel (076)-555-0183</p>
      <p>dov@bright-loom.co.il</p>
    </div>
    <div class="person">Dov Marom<small class="he">מנהל שיווק ופיתוח</small></div>
  </section>
  <section class="piece card-back" style="left:355px;top:103px">
    <div class="strip"></div><div class="mark"></div>
  </section>

  <!-- business cards, row 2 -->
  <section class="piece card-front" style="left:91px;top:259px">
    <svg class="wave" viewBox="0 0 245 137" aria-hidden="true"><path d="M0 110 Q120 96 245 70 L245 137 L0 137 Z" fill="var(--red)"/></svg>
    <div class="silver top"></div>
    <div class="brand"><span class="brand-square"></span>brightloom</div>
    <p class="tagline he">תכנון פיתוח בניית אירוח וקידום אתרים במנועי חיפוש וברשתות.</p>
    <div class="contacts">
      <p>Halavan 42 St, Ramat Noga</p>
      <p>USA (315)-555-0162</p>
      <p>www.bright-loom.co.il</p>
    </div>
    <div class="person">Dov Marom<small>(052)-555-0139</small></div>
  </section>
  <section class="piece card-back" style="left:355px;top:259px">
    <div class="strip"></div><div class="mark"></div>
  </section>

  <!-- letterhead -->
  <section class="piece letterhead">
    <div class="brand"><span class="brand-square"></span>brightloom</div>
    <p class="tagline he">תכנון פיתוח בניית אירוח וקידום אתרים במנועי חיפוש וברשתות.</p>
    <div class="head-info">
      <p class="he">רחוב הלבן 42, א.ת. רמת נוגה</p>
      <p>Halavan 42 St, Ramat Noga</p>
      <p>(888)-555-0147 · www.bright-loom.co.il</p>
    </div>
    <div class="mark"></div>
    <svg class="foot" viewBox="0 0 456 160" aria-hidden="true">
      <path d="M0 20 L0 160 L456 160 L456 20 Q228 120 0 20 Z" fill="var(--red)"/>
    </svg>
  </section>

  <!-- envelope -->
  <section class="piece envelope">
    <div class="flap"></div><div class="flap-dot"></div>
    <div class="brand"><span class="brand-square"></span>brightloom</div>
    <p class="tagline he">תכנון פיתוח בניית אירוח וקידום אתרים במנועי חיפוש וברשתות.</p>
    <div class="mark"></div>
    <div class="silver"></div>
    <div class="foot-info">
      <p>USA only (888)-555-0147</p>
      <p>Halavan 42 St, Ramat Noga</p>
      <p>(076)-555-0183</p>
      <p>www.bright-loom.co.il</p>
    </div>
  </section>

</main>
</body>
</html>
```